Assessment Report cover design and formatting

This report is for senior executives and provides leaders with detailed insight into their capabilities and skills. The cover should have space for the date and name of the person doing the assessment. We are looking to modernise the report cover design. We would like the report to be our company colours if possible. The work will likely expand once the cover is done to other parts of the report, ie. the format and layout of the report etc.

Company colours:
Primary colours:
• Blue #0D47A1, #115CD0, #90B6ED, #EEf3FB
• Green #0D91A1, #47A10D, #324C196, #0DA11D
Additional colours:
• Purple #A10D91
• Brown #A1670D
• Red #A10D47

Target Market(s)

Executives

Industry/Entity Type

Consulting, leadership development

Colors
0094D4
00A9DD
6FCCEA
C7EBF8
E9F6FB
00AB8E
00BBA5
67D7C9
C6EFE9
E9F9F6
E54698
E96AAD
F1A4CE
F9D9EA
FCEFF6
6B429C
8869AF
B7A5CE
E3DAEB
F3F0F8

Requirements
Must have
• The report cover should have space for name of user, the date and company logo. Cover should be in A4 size.

```html
<!DOCTYPE html>
<html lang="en">
<head>
<meta charset="utf-8">
<title>Growth Leader Assessment – Insight Report Cover</title>
<link rel="stylesheet" href="https://fonts.googleapis.com/css2?family=Bebas+Neue&family=Montserrat:wght@400;500;800&display=swap">
<style>
  :root {
    --stage: #d6d6d6;
    --ink-dark: #1f2326;
    --photo-slate: #3a4350;
    --brand-green: #16a12a;
    --brand-green-deep: #0da11d;
    --brand-teal: #0d91a1;
    --brand-blue: #115cd0;
    --brand-blue-deep: #0d47a1;
    --paper: #ffffff;
    --logo-ink: #1a3fa6;
  }
  * { box-sizing: border-box; margin: 0; padding: 0; }
  html, body { width: 1200px; height: 719px; overflow: hidden; }
  body { background: var(--stage); position: relative; }

  .cover {
    position: absolute; left: 366px; top: 30px;
    width: 467px; height: 660px; overflow: hidden;
    background: var(--photo-slate);
    box-shadow: 0 12px 30px rgba(0,0,0,.28);
  }
  .cover-art { position: absolute; inset: 0; width: 100%; height: 100%; }

  .title-growth {
    position: absolute; left: 202px; top: 78px;
    font: 500 50px/1 "Montserrat", sans-serif; color: var(--paper);
  }
  .title-leader {
    position: absolute; left: 203px; top: 132px;
    font: 800 55px/1 "Montserrat", sans-serif; color: var(--brand-green);
    letter-spacing: 1px;
  }
  .title-assessment {
    position: absolute; left: 194px; top: 192px; width: 250px; height: 66px;
    background: linear-gradient(90deg, var(--brand-blue) 0%, var(--brand-blue) 72%, rgba(17,92,208,0) 100%);
    font: 400 60px/70px "Bebas Neue", sans-serif; color: var(--paper);
    padding-left: 14px; letter-spacing: .5px;
  }

  .report-label {
    position: absolute; left: 49px; top: 408px; width: 190px; height: 38px;
    background: linear-gradient(90deg, var(--brand-green-deep) 0%, var(--brand-green-deep) 62%, rgba(13,161,29,0) 100%);
    font: 400 25px/40px "Bebas Neue", sans-serif; color: var(--paper);
    padding-left: 9px; letter-spacing: .3px;
  }
  .report-month {
    position: absolute; left: 30px; top: 480px; width: 60px; height: 30px;
    transform: rotate(-90deg);
    font: 400 32px/30px "Bebas Neue", sans-serif; color: var(--brand-green);
    text-align: center;
  }
  .report-year {
    position: absolute; left: 80px; top: 447px;
    font: 400 86px/1 "Bebas Neue", sans-serif; letter-spacing: 1px;
    background: linear-gradient(180deg, var(--brand-green) 0%, var(--brand-teal) 50%, var(--brand-blue) 100%);
    -webkit-background-clip: text; background-clip: text; color: transparent;
  }

  .company-mark {
    position: absolute; right: 29px; top: 543px; text-align: right;
    font-family: "Montserrat", sans-serif; font-weight: 500; color: var(--logo-ink);
  }
  .company-name { font-size: 19px; line-height: 1.1; letter-spacing: 2.5px; }
  .company-name-second { display: flex; align-items: center; justify-content: flex-end; gap: 6px; }
  .company-dot { width: 9px; height: 9px; border-radius: 50%; background: var(--logo-ink); }
  .company-tagline { font-size: 8.5px; letter-spacing: 2.6px; margin-top: 5px; }
</style>
</head>
<body>
  <main class="cover">
    <svg class="cover-art" viewBox="0 0 921 1302" preserveAspectRatio="none">
      <defs>
        <linearGradient id="meeting-tone" x1="0" y1="0" x2="1" y2="1">
          <stop offset="0" stop-color="#2e3642"/>
          <stop offset="1" stop-color="#4a5563"/>
        </linearGradient>
        <linearGradient id="texture-tone" x1="0" y1="0" x2="1" y2="1">
          <stop offset="0" stop-color="#2a2c2e"/>
          <stop offset=".5" stop-color="#3a3733"/>
          <stop offset="1" stop-color="#1c2226"/>
        </linearGradient>
        <linearGradient id="swoosh-tone" x1="0" y1="0" x2="1" y2="0">
          <stop offset="0" stop-color="#12a032"/>
          <stop offset=".45" stop-color="#0d9a80"/>
          <stop offset="1" stop-color="#0a6fc4"/>
        </linearGradient>
        <linearGradient id="corner-edge" x1="1" y1="0" x2="0" y2="1">
          <stop offset="0" stop-color="#115cd0"/>
          <stop offset="1" stop-color="#0d47a1"/>
        </linearGradient>
      </defs>

      <g role="img" aria-label="Photo of executives in a bright meeting room, softened with a dark slate overlay">
        <rect width="921" height="1302" fill="url(#meeting-tone)"/>
      </g>

      <path d="M0,580 C170,770 420,880 660,872 C790,866 880,830 921,805 V0 H0 Z" fill="var(--paper)"/>
      <path d="M0,490 C140,690 400,820 660,815 C790,810 880,790 921,778 V0 H0 Z" fill="url(#swoosh-tone)"/>

      <g role="img" aria-label="Dark abstract architectural texture behind the title">
        <path d="M0,370 C110,590 370,750 650,760 C790,765 880,755 921,740 V0 H0 Z" fill="url(#texture-tone)"/>
      </g>

      <path d="M310,1302 C360,1100 520,930 921,868 V1302 Z" fill="url(#corner-edge)"/>
      <path d="M332,1302 C385,1110 545,950 921,884 V1302 Z" fill="var(--brand-green-deep)"/>
      <path d="M400,1302 C440,1120 600,978 921,886 V1302 Z" fill="var(--paper)"/>
    </svg>

    <h1 class="cover-title">
      <span class="title-growth">Growth</span>
      <span class="title-leader">LEADER</span>
      <span class="title-assessment">ASSESSMENT</span>
    </h1>

    <div class="report-label">Insight Report For</div>
    <div class="report-month">AUG</div>
    <div class="report-year">2023</div>

    <div class="company-mark">
      <div class="company-name">northfield</div>
      <div class="company-name company-name-second"><span class="company-dot"></span>ADVISORY</div>
      <div class="company-tagline">Partners in Progress</div>
    </div>
  </main>
</body>
</html>
```